Business Card Design Project

I need a business card design for an Organic drive thru coffee kiosk. We will serve organic coffee, teas & smoothies and will serve healthy breakfast food/snacks for people on the go.
I want the card to have 2-3 colors max (earthy colors like browns, greens and so on).
I have attached the logo I want used and would love to play off the theme of "balance."
Include:
Tidy-Kettle Coffee
address: 4820 Gorvin Ct. Raleigh, NC 27583
phone: 919-731-4062
website: www.tidy-kettle.com (website is not up yet but still include it on card)
email: Rosalind@tidy-kettle.com
I want one of the following sayings somewhere on the card (the front or back is fine):
"Eat & Drink Tidy, on the run!"
"Break the fast with Tidy-Kettle"
Maybe on the back list what we offer:
-Organic coffee, espresso & tea
-Blendora smoothies & protein shakes
-Zesty Pour (100% fresh local fruit and veggies)
-Tender Nibs

```html
<!DOCTYPE html>
<html lang="en">
<head>
<meta charset="utf-8">
<title>Tidy-Kettle Coffee – Business Card</title>
<link href="https://fonts.googleapis.com/css2?family=Delius&family=Source+Sans+3:wght@600&display=swap" rel="stylesheet">
<style>
  :root {
    --backdrop: #e9e4dc;
    --green-light: #93c84e;
    --green-dark: #6aa33a;
    --brown: #3f2a1e;
    --brown-band: #3a2a1f;
    --rust: #8a4a2e;
    --mark: #7a4630;
    --band-text: #93c84e;
  }
  * { margin: 0; padding: 0; box-sizing: border-box; }
  html, body { width: 1200px; height: 1181px; overflow: hidden; }
  body { background: var(--backdrop); position: relative; font-family: "Delius", "Trebuchet MS", sans-serif; color: var(--brown); }

  .card {
    position: absolute; left: 242px; width: 716px; height: 411px;
    border-radius: 28px; overflow: hidden;
    background: radial-gradient(ellipse 60% 70% at 50% 40%, var(--green-light), var(--green-dark));
  }
  .card--front { top: 138px; }
  .card--back { top: 622px; }

  .abs { position: absolute; left: 0; right: 0; text-align: center; }
  .brand-dot { position: absolute; border-radius: 50%; background: var(--mark); }
  .brand-name { color: var(--brown); line-height: 1; }
  .brand-tagline { font-family: "Source Sans 3", Arial, sans-serif; font-weight: 600; color: var(--rust); }

  /* front */
  .card--front .brand-dot { left: 322px; top: 124px; width: 72px; height: 72px; }
  .card--front .brand-name { top: 208px; font-size: 50px; }
  .card--front .brand-tagline { top: 273px; font-size: 14px; letter-spacing: 2.6px; }

  .services { position: absolute; left: 160px; width: 396px; top: 330px; height: 60px; }
  .services__rule { position: absolute; height: 3px; background: var(--brown); }
  .services__rule--top-left { left: 0; top: 7px; width: 138px; }
  .services__rule--top-right { right: 0; top: 7px; width: 140px; }
  .services__rule--bottom { left: 0; right: 0; top: 55px; }
  .services__title { position: absolute; left: 0; right: 0; top: 0; text-align: center; font-size: 12px; }
  .services__list { position: absolute; left: -10px; right: -10px; top: 16px; text-align: center; font-size: 12px; line-height: 17px; }
  .side-dot { position: absolute; top: 344px; width: 32px; height: 32px; border-radius: 50%; background: var(--mark); }
  .side-dot--left { left: 119px; }
  .side-dot--right { left: 567px; }

  /* back */
  .band { position: absolute; left: 0; right: 0; height: 50px; background: var(--brown-band);
          display: flex; align-items: center; justify-content: center; gap: 8px;
          color: var(--band-text); font-size: 15px; }
  .band--top { top: 0; }
  .band--bottom { bottom: 0; height: 48px; }
  .band__dot { width: 14px; height: 14px; border-radius: 50%; background: var(--mark); }

  .card--back .brand-dot { left: 328px; top: 150px; width: 54px; height: 54px; }
  .card--back .brand-name { top: 212px; font-size: 37px; }
  .card--back .brand-tagline { top: 256px; font-size: 10px; letter-spacing: 2px; }

  .contact { position: absolute; top: 291px; font-size: 12px; line-height: 17px; }
  .contact--address { right: 374px; text-align: right; }
  .contact--reach { left: 376px; text-align: left; }
  .contact__divider { position: absolute; left: 357px; top: 286px; width: 2px; height: 42px; background: var(--brown); }
  .website { top: 344px; font-size: 12px; }
</style>
</head>
<body>

<section class="card card--front">
  <span class="brand-dot"></span>
  <div class="abs brand-name">Tidy-Kettle</div>
  <div class="abs brand-tagline">ORGANIC COFFEE + CAFE</div>

  <span class="side-dot side-dot--left"></span>
  <div class="services">
    <span class="services__rule services__rule--top-left"></span>
    <span class="services__rule services__rule--top-right"></span>
    <div class="services__title">Services we offer :</div>
    <div class="services__list">
      - Organic coffee, espresso &amp; tea - Blendora smoothies &amp; protein shakes<br>
      - Zesty Pour (100% fresh local fruit and veggies) - Tender Nibs
    </div>
    <span class="services__rule services__rule--bottom"></span>
  </div>
  <span class="side-dot side-dot--right"></span>
</section>

<section class="card card--back">
  <div class="band band--top"><span class="band__dot"></span>Break the fast with Tidy-Kettle<span class="band__dot"></span></div>

  <span class="brand-dot"></span>
  <div class="abs brand-name">Tidy-Kettle</div>
  <div class="abs brand-tagline">ORGANIC COFFEE + CAFE</div>

  <div class="contact contact--address">4820 Gorvin Ct. Raleigh,<br>NC 27583</div>
  <span class="contact__divider"></span>
  <div class="contact contact--reach">919-731-4062<br>Rosalind@tidy-kettle.com</div>
  <div class="abs website">www.tidy-kettle.com</div>

  <div class="band band--bottom"><span class="band__dot"></span>Eat &amp; Drink Tidy, on the run!<span class="band__dot"></span></div>
</section>

</body>
</html>
```